Looking for a clean, modern, and professional business card design that reflects Valtrin Systems

The design should include the company logo, contact details, and align with our brand identity. Please use a sophisticated and minimalist style, incorporating [specific colors, if applicable]. Creativity is welcome, but the card must maintain a polished and professional appearance.

Details to Include:

Name: Lou Marchetti
Title: VP Sales / Operations
Company: Valtrin Systems
Phone: 304.617.2285
Email: lou@valtrinsystems.example
Website: www.valtrinsystems.example

```html
<!DOCTYPE html>
<html lang="en">
<head>
<meta charset="utf-8">
<title>Valtrin Systems – Business Card</title>
<link href="https://fonts.googleapis.com/css2?family=Poppins:wght@400;500;600&display=swap" rel="stylesheet">
<style>
  :root {
    --stage: #444444;
    --front-side: #161b21;
    --front-band: #050505;
    --back-paper: #e8e7e8;
    --brand-blue: #3a74b8;
    --ink: #111111;
    --ink-soft: #2f2f2f;
    --white: #ffffff;
  }
  * { box-sizing: border-box; margin: 0; padding: 0; }
  html, body { width: 1200px; height: 1000px; overflow: hidden; }
  body {
    position: relative;
    background: var(--stage);
    font-family: "Poppins", sans-serif;
  }
  .card {
    position: absolute;
    left: 211px;
    width: 778px;
    height: 444px;
    border-radius: 28px;
    overflow: hidden;
  }
  .card-front {
    top: 43px;
    background: radial-gradient(ellipse at center, #1c232b 0%, var(--front-side) 55%, #0b0d10 100%);
  }
  .front-band {
    position: absolute;
    left: 223px;
    top: 0;
    width: 332px;
    height: 100%;
    background: var(--front-band);
  }
  .wordmark {
    position: absolute;
    font-weight: 600;
    letter-spacing: 1px;
    white-space: nowrap;
    transform: translate(-50%, -50%);
  }
  .front-wordmark {
    left: 389px;
    top: 219px;
    font-size: 34px;
    color: var(--white);
  }
  .card-back {
    top: 513px;
    background: var(--back-paper);
  }
  .back-divider {
    position: absolute;
    left: 417px;
    top: 30px;
    width: 60px;
    height: 390px;
    background: radial-gradient(ellipse at left center, rgba(0,0,0,0.16) 0%, rgba(0,0,0,0) 70%);
    border-left: 1px solid rgba(0,0,0,0.06);
  }
  .contact-block {
    position: absolute;
    left: 0;
    top: 84px;
    width: 448px;
    text-align: center;
  }
  .person-name {
    font-size: 28px;
    font-weight: 600;
    color: var(--brand-blue);
    line-height: 1.2;
  }
  .person-title {
    font-size: 21px;
    font-weight: 500;
    color: var(--ink);
    margin-top: 2px;
  }
  .contact-lines { list-style: none; margin-top: 28px; }
  .contact-lines li {
    font-size: 20px;
    color: var(--ink-soft);
    line-height: 47px;
  }
  .contact-icons {
    position: absolute;
    left: 438px;
    top: 187px;
    width: 24px;
  }
  .contact-icons svg { display: block; width: 22px; height: 22px; margin-bottom: 25px; }
  .back-wordmark {
    left: 607px;
    top: 225px;
    font-size: 30px;
    color: var(--ink);
  }
</style>
</head>
<body>
  <section class="card card-front" aria-label="Card front">
    <div class="front-band"></div>
    <div class="wordmark front-wordmark">Valtrin Systems</div>
  </section>

  <section class="card card-back" aria-label="Card back">
    <div class="back-divider"></div>
    <div class="contact-block">
      <h1 class="person-name">Lou Marchetti</h1>
      <p class="person-title">VP Sales / Operations</p>
      <ul class="contact-lines">
        <li>304.617.2285</li>
        <li>lou@valtrinsystems.example</li>
        <li>www.valtrinsystems.example</li>
      </ul>
    </div>
    <div class="contact-icons">
      <svg viewBox="0 0 24 24" aria-label="Phone"><path fill="#3a74b8" d="M6.6 10.8a15 15 0 0 0 6.6 6.6l2.2-2.2a1 1 0 0 1 1-.25 11.4 11.4 0 0 0 3.6.57 1 1 0 0 1 1 1V20a1 1 0 0 1-1 1A17 17 0 0 1 3 4a1 1 0 0 1 1-1h3.5a1 1 0 0 1 1 1c0 1.25.2 2.45.57 3.6a1 1 0 0 1-.25 1z"/></svg>
      <svg viewBox="0 0 24 24" aria-label="Email"><path fill="#3a74b8" d="M2 5h20v14H2z"/><path fill="none" stroke="#e8e7e8" stroke-width="1.6" d="M2.5 5.5 12 13l9.5-7.5"/></svg>
      <svg viewBox="0 0 24 24" aria-label="Website"><g fill="none" stroke="#3a74b8" stroke-width="2"><circle cx="12" cy="12" r="9"/><ellipse cx="12" cy="12" rx="4" ry="9"/><path d="M3 12h18M4.5 7.5h15M4.5 16.5h15"/></g></svg>
    </div>
    <div class="wordmark back-wordmark">Valtrin Systems</div>
  </section>
</body>
</html>
```